Meridian Path Advisors WordPress Site.

We need a modern, consultative looking, and exciting WordPress site to show case our new consulting company called Meridian Path Advisors LLC. Meridian Path Advisors (MPA) based in Southern California, provides expertise for companies who are interested in building an indirect sales channel. Some may think of this as building a Partner Program. Our offerings include, Discovery, Strategic Planning, Goals and Objective Setting, Partner Recruitment & Enablement, Team Building, and Outcome Definition. We purchased our logo from Loomgrove which is attached. The colors are Blue and Grey. The final design should convey a fresh, modern, and exciting look. Don't forget this is a consulting company, so we can't get too "wild". Hopefully we can come up with a nice balance. We attached our logo (two versions) and our Founder's photo. Please let us know what else you need to get started. I suspect you'll outline the design and we can iterate on the copy. Lastly, we'll be using Veltrahost as our hosting provider.

Target Market(s)

Small to mid-size SaaS Companies.

Industry/Entity Type

Consulting for Indirect Sales Channels

Coding

Coded - Design and coding required

Font styles to use
Other font styles liked:
• Please select a font that compliments the logo. Modern and easy to read.

Colors
0054AA
0677BA
7BADD7
CADEEF
E8F1F8
00AB8E
00BBA5
67D7C9
C6EFE9
E9F9F6
FFF300
FFF600
FEFA6F
FFFEC7
FFFEE8

Requirements
Must have
• My project must include the following pages. Homepage, About Us, Offerings & Services, and Contact Us
Nice to have
• Clean, bright and modern look. Area(s) and ability to insert video or blog posts.
Should not have
• Should not contain clutter. Black background.

```html
<!DOCTYPE html>
<html lang="en">
<head>
<meta charset="utf-8">
<title>Meridian Path Advisors — Control Your Future</title>
<link rel="stylesheet" href="https://fonts.googleapis.com/css2?family=Orbitron:wght@500;600;700;800&family=Poppins:wght@400;500;600;700&display=swap">
<style>
:root{
  --blue:#0a3f9c;
  --blue-deep:#0a3a95;
  --ink:#222;
  --grey:#555;
  --hex:#eeeff1;
  --num:#9a9a9a;
  --line:#c9c9c9;
  --field:#2a2b2d;
  --white:#fff;
}
*{box-sizing:border-box;margin:0;padding:0}
html,body{width:1200px;height:3628px;overflow:hidden}
body{position:relative;font-family:"Poppins",sans-serif;color:var(--ink);background:var(--white)}
.abs{position:absolute}
.display{font-family:"Orbitron",sans-serif;font-weight:800;text-transform:uppercase;letter-spacing:1px}

/* header */
.site-header{position:absolute;left:0;top:0;width:1200px;height:72px;background:var(--white)}
.brand{left:88px;top:20px;display:flex;align-items:center;gap:10px;font-weight:600;font-size:19px;color:var(--blue);letter-spacing:.5px}
.brand-dot{width:30px;height:30px;border-radius:50%;background:var(--blue)}
.nav{right:88px;top:27px;display:flex;gap:32px;font-size:12.5px;font-weight:500;color:#555;letter-spacing:.3px}
.nav .current{color:var(--blue);font-weight:600}

/* hero */
.hero{left:0;top:72px;width:1200px;height:687px;background:linear-gradient(90deg,#f1f3f6 0%,#e6eaf0 45%,#9aa4b4 75%,#5b6576 100%)}
.hero-title{left:85px;top:334px;font-size:48px;line-height:48px;color:var(--blue)}
.hero-sub{left:86px;top:436px;font-size:14px;color:#444}

/* story */
.section-title{width:1200px;left:0;text-align:center;font-size:44px;line-height:52px;color:var(--blue)}
.timeline{left:581px;top:1020px;width:0;height:585px;border-left:2px dashed var(--line)}
.dot{width:14px;height:14px;border-radius:50%;background:var(--blue);left:575px}
.hex{width:190px;height:200px}
.hex text{font-family:"Poppins",sans-serif;font-weight:700;font-size:120px;fill:var(--num)}
.story-h{font-family:"Orbitron",sans-serif;font-weight:600;font-size:18px;line-height:26px;text-transform:uppercase;color:var(--ink);letter-spacing:.5px;white-space:nowrap}
.story-p{font-size:13.5px;line-height:20px;color:var(--grey);white-space:nowrap}
.right{text-align:right}

/* testimonials */
.testimonials{left:0;top:1864px;width:1200px;height:605px;background:var(--blue-deep)}
.avatar{position:absolute;border-radius:50%;border:3px solid var(--white);background:#b9a48e}
.quote{left:564px;top:2103px;width:530px;font-size:14.5px;line-height:22.5px;color:var(--white)}
.person{left:564px;top:2254px;color:var(--white);font-size:20px;line-height:26px}
.person b{font-weight:700}
.arrow{width:40px;height:40px;border-radius:50%;background:var(--white);top:2315px;display:flex;align-items:center;justify-content:center}

/* about */
.about-title{left:88px;top:2648px;font-size:44px;color:var(--blue)}
.about-p{left:88px;top:2714px;width:475px;font-size:14.5px;line-height:21.5px;color:var(--grey)}
.btn-outline{left:88px;top:2842px;width:136px;height:50px;border:2px solid #ccc;font-size:14px;font-weight:500;color:var(--ink);display:flex;align-items:center;justify-content:center}
.laptop{left:580px;top:2588px;width:584px;height:330px;background:linear-gradient(180deg,#eef0f2,#d9dcdf);border-radius:12px}

/* contact */
.contact{left:0;top:3024px;width:1200px;height:604px;background:linear-gradient(135deg,#505153 0%,#3a3b3d 50%,#2c2d2f 100%)}
.contact-title{left:88px;top:3194px;font-size:40px;line-height:46px;color:var(--white)}
.contact-info{left:88px;top:3293px;font-size:15px;line-height:25.5px;color:var(--white)}
.contact-info li{list-style:none;display:flex;align-items:center;gap:8px}
.social{left:88px;top:3392px;display:flex;gap:14px}
.social span{width:12px;height:12px;border-radius:50%;background:var(--white)}
.field{background:var(--field);color:var(--white);font-size:14px;padding:14px 22px}
.btn-solid{left:568px;top:3417px;width:143px;height:50px;background:var(--blue);color:var(--white);font-size:13px;font-weight:700;display:flex;align-items:center;justify-content:center}
.copyright{left:0;width:1200px;top:3586px;text-align:center;color:var(--white);font-size:15px}
.to-top{left:1137px;top:3542px;width:36px;height:36px;border-radius:50%;background:var(--blue);display:flex;align-items:center;justify-content:center}
</style>
</head>
<body>

<header class="site-header">
  <div class="abs brand"><span class="brand-dot"></span>MERIDIAN PATH ADVISORS</div>
  <nav class="abs nav">
    <span class="current">HOME</span><span>ABOUT US</span><span>OFFERINGS &amp; SERVICES</span><span>CONTACT US</span>
  </nav>
</header>

<section class="abs hero" role="img" aria-label="Photo of two business colleagues reviewing a tablet at an office desk"></section>
<h1 class="abs hero-title display">Control<br>Your Future.</h1>
<p class="abs hero-sub">Create. Optimize. Unleash the Power of Partnerships &amp; Alliances.</p>

<h2 class="abs section-title display" style="top:884px">Our Story</h2>
<div class="abs timeline"></div>
<span class="abs dot" style="top:1014px"></span>
<span class="abs dot" style="top:1195px"></span>
<span class="abs dot" style="top:1390px"></span>
<span class="abs dot" style="top:1598px"></span>

<svg class="abs hex" style="left:271px;top:955px" viewBox="0 0 190 200"><polygon points="95,12 172,56 172,144 95,188 18,144 18,56" fill="var(--hex)" stroke="var(--hex)" stroke-width="22" stroke-linejoin="round"/><text x="95" y="142" text-anchor="middle">1</text></svg>
<h3 class="abs story-h" style="left:618px;top:1009px">Do you worry about how<br>you’re going to make your revenue<br>number while managing costs?</h3>
<p class="abs story-p" style="left:618px;top:1091px">You’re not alone. Most business leaders wrestle with the same concern.</p>

<h3 class="abs story-h right" style="left:60px;top:1191px;width:486px">What options do you have?</h3>
<p class="abs story-p right" style="left:46px;top:1222px;width:500px">You can hire more salespeople and business development reps.<br>You can invest in Searchwell Ads, marketing campaigns, purchase<br>lead lists, conduct webinars, increase social marketing, train your<br>sales team, add solution engineers, etc. You get the picture...</p>
<svg class="abs hex" style="left:720px;top:1140px" viewBox="0 0 190 200"><polygon points="95,12 172,56 172,144 95,188 18,144 18,56" fill="var(--hex)" stroke="var(--hex)" stroke-width="22" stroke-linejoin="round"/><text x="95" y="142" text-anchor="middle">2</text></svg>

<svg class="abs hex" style="left:290px;top:1346px" viewBox="0 0 190 200"><polygon points="95,12 172,56 172,144 95,188 18,144 18,56" fill="var(--hex)" stroke="var(--hex)" stroke-width="22" stroke-linejoin="round"/><text x="95" y="142" text-anchor="middle">3</text></svg>
<h3 class="abs story-h" style="left:623px;top:1385px">Have you considered<br>scaling your business through<br>partnerships and alliances?</h3>
<p class="abs story-p" style="left:623px;top:1468px">Do you really know what that means? Does your strategic plan<br>include a robust indirect sales channel? If not, it should.</p>

<h3 class="abs story-h right" style="left:60px;top:1597px;width:486px">What options do you have?</h3>
<p class="abs story-p right" style="left:43px;top:1628px;width:500px">Lead generation, Deal acceleration, Higher close ratios, Cost<br>management, Improved margin, Scalability, Growth</p>
<p class="abs story-p right" style="left:43px;top:1678px;width:500px">Meridian Path Advisors can help you to think through the<br>challenge and outline a plan that works for your company. Our<br>mission is to help companies to control their future by leveraging<br>an effective indirect sales channel. Contact us to learn more.</p>
<svg class="abs hex" style="left:742px;top:1573px" viewBox="0 0 190 200"><polygon points="95,12 172,56 172,144 95,188 18,144 18,56" fill="var(--hex)" stroke="var(--hex)" stroke-width="22" stroke-linejoin="round"/><text x="95" y="142" text-anchor="middle">4</text></svg>

<section class="abs testimonials"></section>
<h2 class="abs section-title display" style="top:1984px;color:var(--white)">Testimonials</h2>
<div role="img" aria-label="Cluster of client portrait photos">
  <span class="avatar" style="left:231px;top:2054px;width:32px;height:32px"></span>
  <span class="avatar" style="left:398px;top:2086px;width:28px;height:28px"></span>
  <span class="avatar" style="left:190px;top:2133px;width:112px;height:112px"></span>
  <span class="avatar" style="left:341px;top:2170px;width:42px;height:42px"></span>
  <span class="avatar" style="left:432px;top:2178px;width:30px;height:30px"></span>
  <span class="avatar" style="left:428px;top:2220px;width:72px;height:72px"></span>
  <span class="avatar" style="left:237px;top:2264px;width:52px;height:52px"></span>
  <span class="avatar" style="left:320px;top:2274px;width:86px;height:86px"></span>
  <span class="avatar" style="left:402px;top:2375px;width:44px;height:44px"></span>
</div>
<p class="abs quote">Lorem Ipsum is simply dummy text of the printing and typesetting industry. Lorem Ipsum has been the industry's standard dummy text ever since the 1500s, when an unknown printer took a galley of type and scrambled it to make a type specimen book. It has survived not only five centuries, but also the leap into electronic typesetting, remaining essentially unchanged. It was popularised</p>
<div class="abs person"><b>Daniel Reyes</b><br>Co Founder</div>
<span class="abs arrow" style="left:559px"><svg width="16" height="10" viewBox="0 0 16 10"><path d="M15 5H2M6 1 2 5l4 4" fill="none" stroke="#333" stroke-width="1.5"/></svg></span>
<span class="abs arrow" style="left:607px"><svg width="16" height="10" viewBox="0 0 16 10"><path d="M1 5h13M10 1l4 4-4 4" fill="none" stroke="#333" stroke-width="1.5"/></svg></span>

<h2 class="abs about-title display">About Us</h2>
<p class="abs about-p">Lorem Ipsum is simply dummy text of the printing and typesetting industry. Lorem Ipsum has been the industry's standard dummy text ever since the 1500s, when an unknown printer took a galley of type and scrambled it to make a type specimen book. It has survived not only five centuries, but also the leap .</p>
<a class="abs btn-outline">READ MORE</a>
<div class="abs laptop" role="img" aria-label="Laptop showing the Meridian Path Advisors brand on screen"></div>

<section class="abs contact" role="img" aria-label="Dark monochrome photo of people working at a desk"></section>
<h2 class="abs contact-title display">Contact<br>Information</h2>
<ul class="abs contact-info">
  <li><svg width="10" height="12" viewBox="0 0 10 12"><path d="M5 0a4 4 0 0 0-4 4c0 3 4 8 4 8s4-5 4-8a4 4 0 0 0-4-4z" fill="#2f6ad0"/></svg>Some goes address here</li>
  <li><svg width="11" height="9" viewBox="0 0 11 9"><rect width="11" height="9" fill="#2f6ad0"/></svg>hello@meridianpath.example</li>
  <li><svg width="11" height="11" viewBox="0 0 11 11"><path d="M2 0 4 3 3 4.5Q4.5 7 6.5 8L8 7l3 2-1 2Q4 11 0 2z" fill="#2f6ad0"/></svg>+1 555 014 2207</li>
</ul>
<div class="abs social"><span></span><span></span><span></span><span></span></div>
<div class="abs field" style="left:568px;top:3197px;width:265px;height:50px">Name</div>
<div class="abs field" style="left:845px;top:3197px;width:265px;height:50px">Email</div>
<div class="abs field" style="left:568px;top:3258px;width:542px;height:152px">Message</div>
<a class="abs btn-solid">SUBMIT NOW</a>
<p class="abs copyright">©Copyright 2022 | All Rights Reserved</p>
<span class="abs to-top"><svg width="10" height="12" viewBox="0 0 10 12"><path d="M5 12V1M1 5l4-4 4 4" fill="none" stroke="#fff" stroke-width="1.5"/></svg></span>

</body>
</html>
```